Tova Brisk Fitness Coaching Project

I am a personal trainer based in London. My services include one-on-one PT sessions, bootcamps.
I would like the design to be minimalistic. With light colours: white, pink, purple.
I specialise in weight loss, flexibility, mobility.

Tova Penrick
Personal Trainer
Email: tova.penrick@mailgrove.net
tel: 07500 918 243
Instagram: Tova Brisk

Target Market(s)

adults, mostly females (age 18-50).

Industry/Entity Type

Fitness

Contact Information for Business Card

Tova Penrick
Personal Trainer
tel: 07500 918 243
Instagram: Tova Brisk

Font styles to use
Serif

Colors
eea4c8
fbd4d5
fdf9cf
cfeae6
cee9f5

Requirements
Nice to have
• minimalistic style
• easy to read and remember

```html
<!DOCTYPE html>
<html lang="en">
<head>
<meta charset="utf-8">
<title>Tova Penrick – Personal Trainer Business Card</title>
<link rel="stylesheet" href="https://fonts.googleapis.com/css2?family=Open+Sans:wght@400;600;700&display=swap">
<style>
  :root {
    --page-bg: #8d8d8d;
    --card-bg: #ffffff;
    --card-shade: #f1f1f1;
    --accent-pink: #ee4fdf;
    --band-pink: #f06fe6;
    --band-pink-light: #f6a4f0;
    --text-grey: #555555;
    --band-text: #ffffff;
    --photo-warm: #9a6a45;
    --photo-light: #e9d6c4;
    --photo-dark: #3e4a2e;
    --photo-rose: #d9a0a8;
  }

  * { margin: 0; padding: 0; box-sizing: border-box; }

  html, body {
    width: 1200px;
    height: 900px;
    overflow: hidden;
  }

  body {
    background: var(--page-bg);
    font-family: "Open Sans", Arial, sans-serif;
    display: flex;
    align-items: center;
    justify-content: center;
  }

  .business-card {
    position: relative;
    width: 1000px;
    height: 570px;
    background: linear-gradient(180deg, var(--card-bg) 0%, var(--card-shade) 100%);
    overflow: hidden;
  }

  .portrait-area {
    position: absolute;
    top: 0;
    right: 0;
    width: 600px;
    height: 100%;
    background:
      radial-gradient(ellipse 40% 45% at 55% 40%, var(--photo-light) 0%, rgba(233,214,196,0) 70%),
      radial-gradient(ellipse 60% 70% at 60% 55%, var(--photo-warm) 0%, rgba(154,106,69,0) 75%),
      radial-gradient(ellipse 40% 60% at 95% 20%, var(--photo-dark) 0%, rgba(62,74,46,0) 80%),
      radial-gradient(ellipse 45% 40% at 80% 85%, var(--photo-rose) 0%, rgba(217,160,168,0) 80%),
      linear-gradient(90deg, #f2ede8 0%, #cfb8a2 100%);
  }

  .portrait-fade {
    position: absolute;
    top: 0;
    right: 300px;
    width: 420px;
    height: 100%;
    background: linear-gradient(90deg, var(--card-bg) 35%, rgba(255,255,255,0) 100%);
  }

  .contact-block {
    position: absolute;
    left: 60px;
    top: 262px;
  }

  .trainer-name {
    font-size: 33px;
    font-weight: 700;
    color: var(--accent-pink);
    letter-spacing: 0.5px;
    line-height: 1.1;
  }

  .trainer-role {
    font-size: 23px;
    font-weight: 400;
    color: var(--text-grey);
    letter-spacing: 0.5px;
    margin-top: 4px;
  }

  .contact-list {
    list-style: none;
    margin-top: 22px;
  }

  .contact-item {
    display: flex;
    align-items: center;
    gap: 14px;
    font-size: 22px;
    color: var(--text-grey);
    line-height: 1.35;
  }

  .contact-icon {
    width: 20px;
    height: 20px;
    flex-shrink: 0;
  }

  .social-mark {
    width: 18px;
    height: 18px;
    background: var(--accent-pink);
    border-radius: 4px;
    flex-shrink: 0;
    margin-left: 1px;
    margin-right: 1px;
  }

  .services-band {
    position: absolute;
    left: 0;
    bottom: 0;
    width: 100%;
    height: 118px;
    background: linear-gradient(180deg, var(--band-pink-light) 0%, var(--band-pink) 45%, var(--band-pink) 100%);
    opacity: 0.95;
    display: flex;
    align-items: flex-end;
    padding: 0 0 22px 60px;
  }

  .services-text {
    font-size: 24px;
    font-weight: 600;
    color: var(--band-text);
  }
</style>
</head>
<body>
  <div class="business-card">
    <div class="portrait-area" role="img" aria-label="Photo of the trainer smiling outdoors in warm sunlight"></div>
    <div class="portrait-fade"></div>

    <div class="contact-block">
      <h1 class="trainer-name">TOVA PENRICK</h1>
      <p class="trainer-role">PERSONAL TRAINER</p>
      <ul class="contact-list">
        <li class="contact-item">
          <svg class="contact-icon" viewBox="0 0 20 20" aria-hidden="true">
            <path d="M2 6 Q10 1 18 6 L16 9 L13 8 L13 6.5 Q10 5.5 7 6.5 L7 8 L4 9 Z" fill="var(--accent-pink)"/>
            <path d="M5 11 H15 L17 18 H3 Z" fill="var(--accent-pink)"/>
            <circle cx="10" cy="14" r="2" fill="#ffffff"/>
          </svg>
          <span>07500 918 243</span>
        </li>
        <li class="contact-item">
          <svg class="contact-icon" viewBox="0 0 20 20" aria-hidden="true">
            <rect x="2" y="5" width="16" height="11" rx="1" fill="var(--accent-pink)"/>
            <path d="M2.5 5.5 L10 11 L17.5 5.5" fill="none" stroke="#ffffff" stroke-width="1.4"/>
          </svg>
          <span>tova.penrick@mailgrove.net</span>
        </li>
        <li class="contact-item">
          <span class="social-mark" aria-hidden="true"></span>
          <span>Tova Brisk</span>
        </li>
      </ul>
    </div>

    <div class="services-band">
      <p class="services-text">PT sessions, bootcamps.</p>
    </div>
  </div>
</body>
</html>
```